Life Coaching Business Card

Please check out my website at www.lorettavisbeck.com. Ideally I would like to use the same colors that I used on the site to match my business cards i.e: pink, green, teal, white
I want the final design to include a picture of me and also to be appealing and eye catching. For the picture I submitted, you can crop it smaller to just have my face (exclude my chest) showing.
Industry/Entity Type
Business
Contact Information for Business Card
Loretta Visbeck
Transformational Life Coach
web: www.lorettavisbeck.com
email: loretta@lorettavisbeck.com
Phone: 555-318-7042
Look and feel
Each slider illustrates characteristics of the customer's brand and the style your logo design should communicate.

```html
<!DOCTYPE html>
<html lang="en">
<head>
<meta charset="utf-8">
<title>Loretta Visbeck — Transformational Life Coach</title>
<link rel="stylesheet" href="https://fonts.googleapis.com/css2?family=Cabin:wght@400;500&family=Arimo&display=swap">
<style>
  :root {
    --paper: #ffffff;
    --ink: #111111;
    --panel: #050505;
    --band: #c445c8;
    --band-light: #d866da;
    --pink: #cf47e3;
    --green: #7ee03c;
    --photo-dark: #2a2a2a;
    --photo-light: #b8b8b8;
    --white: #ffffff;
  }
  * { margin: 0; padding: 0; box-sizing: border-box; }
  html, body { width: 1200px; height: 702px; overflow: hidden; background: var(--paper); }
  .card {
    position: relative; width: 1200px; height: 702px;
    background: var(--paper);
    font-family: "Cabin", sans-serif;
    color: var(--ink);
  }
  .header-art { position: absolute; left: 0; top: 0; width: 1200px; height: 207px; }
  .arc-text { font-family: "Cabin", sans-serif; font-size: 31px; fill: var(--ink); }
  .brand-name { font-family: "Cabin", sans-serif; font-size: 18px; fill: var(--pink); }
  .methods {
    position: absolute; left: 402px; top: 76px; width: 400px;
    text-align: center; font-size: 25px; line-height: 26px;
  }
  .phone {
    position: absolute; left: 868px; top: 143px; width: 220px;
    text-align: center; font-size: 30px; letter-spacing: 0.5px;
  }
  .band {
    position: absolute; left: 27px; width: 1147px;
    background: repeating-linear-gradient(90deg, var(--band) 0 3px, var(--band-light) 3px 5px);
  }
  .band-top { top: 207px; height: 30px; }
  .band-bottom { top: 648px; height: 32px; }
  .panel {
    position: absolute; left: 27px; top: 237px; width: 1147px; height: 411px;
    background: var(--panel);
  }
  .tagline {
    position: absolute; left: 42px; top: 243px;
    font-size: 28px; color: var(--green); white-space: nowrap;
  }
  .website {
    position: absolute; left: 119px; top: 325px;
    font-family: "Arimo", sans-serif; font-size: 47px; color: var(--pink); white-space: nowrap;
  }
  .email {
    position: absolute; left: 161px; top: 372px;
    font-size: 22px; color: var(--white); white-space: nowrap;
  }
  .hours-title {
    position: absolute; left: 74px; top: 442px;
    font-size: 41px; color: var(--green); white-space: nowrap;
  }
  .hours { position: absolute; left: 76px; top: 498px; list-style: none; color: var(--white); }
  .hours li { font-size: 29px; line-height: 40px; white-space: nowrap; }
  .hours li:nth-child(2) { padding-left: 5px; }
  .coach-name {
    position: absolute; left: 855px; top: 244px; width: 300px;
    text-align: center; font-size: 35px; color: var(--white); white-space: nowrap;
  }
  .portrait {
    position: absolute; left: 855px; top: 290px; width: 290px; height: 356px;
    background: radial-gradient(ellipse at 45% 45%, var(--photo-light) 0%, #7a7a7a 45%, var(--photo-dark) 85%, var(--panel) 100%);
  }
</style>
</head>
<body>
<div class="card">
  <svg class="header-art" viewBox="0 0 1200 207" aria-hidden="false">
    <defs>
      <path id="arc-role" d="M 80 186 A 185 175 0 0 1 407 176"/>
      <path id="arc-contact" d="M 813 176 A 180 170 0 0 1 1142 182"/>
    </defs>
    <text class="arc-text"><textPath href="#arc-role" startOffset="50%" text-anchor="middle">Transformational Life Coach</textPath></text>
    <text class="arc-text"><textPath href="#arc-contact" startOffset="50%" text-anchor="middle">Questions Or Appointment</textPath></text>
    <circle cx="236" cy="132" r="15" fill="var(--pink)"/>
    <text class="brand-name" x="236" y="172" text-anchor="middle">Loretta Visbeck</text>
  </svg>

  <div class="methods">
    <div>Transformational&nbsp; Coaching Method</div>
    <div>Neuro Linguistic Programming</div>
    <div>Positive Psychology</div>
    <div>Ontological Coaching</div>
  </div>
  <div class="phone">555-318-7042</div>

  <div class="band band-top"></div>
  <div class="panel"></div>
  <div class="band band-bottom"></div>

  <p class="tagline">Health, Strength, &amp; Balance For Your Mind And Soul.</p>
  <p class="website">www.lorettavisbeck.com</p>
  <p class="email">Contact Me: loretta@lorettavisbeck.com</p>

  <h2 class="hours-title" style="font-weight:400">Coaching Hours:</h2>
  <ul class="hours">
    <li>Monday-Thursday&nbsp; 9AM-8PM</li>
    <li>Friday 9AM-6PM</li>
    <li>Saturday- Sunday 9AM-4PM</li>
  </ul>

  <p class="coach-name">Loretta Visbeck</p>
  <div class="portrait" role="img" aria-label="Black and white portrait photo of Loretta Visbeck with long dark hair"></div>
</div>
</body>
</html>
```